Prestige Car Bodyshop Business Card

We are a car bodyshop based in the UK. Our customer base is mainly prestige high-value vehicles. I am looking for a classy and stylish business card design for my staff to give out to customers, with their direct email and phone number, as well as our main email and phone number with address details

I am also looking to have a general business card design with just our main company address and contact details, but also have a space to add a manufacturer approval logo (i.e Velmora, Orek, Tovalo etc... logo) in the corner somewhere.

I do not particularly want any outlines or pictures of cars on the card, I would just like a quality high-end look.

Please feel free to get in touch if you have any questions or queries?

Many Thanks

Malcolm

Target Market(s)

Prestige vehicle owners

Industry/Entity Type

Automotive

Contact Information for Business Card

I am looking for a classy and stylish business card design for my staff to give out to customers, with their direct email and phone number, as well as our main email and phone number with address details

Font styles to use
Sans Serif

Colors

Designer to choose colors to be used in the design.

Requirements
Nice to have
• I do not particularly want any outlines or pictures of cars on the card, I would just like a quality high-end look.

```html
<!DOCTYPE html>
<html lang="en">
<head>
<meta charset="utf-8">
<title>Harlow Business Cards</title>
<link rel="stylesheet" href="https://fonts.googleapis.com/css2?family=Roboto:wght@300;400;700&display=swap">
<style>
  :root {
    --backdrop: #ecebe8;
    --card: #ffffff;
    --brand-blue: #0f5a99;
    --logo-blue: #0d4d8f;
    --panel-dark: #1f1f21;
    --ink-light: #ffffff;
    --ink-navy: #1b2a5c;
  }
  html, body {
    margin: 0;
    padding: 0;
    width: 1199px;
    height: 1200px;
    overflow: hidden;
    background: var(--backdrop);
    font-family: "Roboto", Arial, sans-serif;
  }
  .card {
    position: absolute;
    left: 206px;
    width: 770px;
    height: 462px;
    background: var(--card);
    box-shadow: 0 6px 18px rgba(0,0,0,0.12);
  }
  .card--front { top: 72px; }
  .card--back { top: 590px; }
  .card svg { display: block; width: 100%; height: 100%; }
  .brand-name { font-family: "Roboto", Arial, sans-serif; font-weight: 300; fill: var(--ink-navy); letter-spacing: 0.5px; }
  .staff-name { font-weight: 700; font-size: 30px; fill: var(--ink-light); }
  .staff-role { font-weight: 400; font-size: 16px; fill: var(--ink-light); }
  .contact-line { font-weight: 300; font-size: 19px; fill: var(--ink-light); }
  .icon { fill: var(--ink-light); }
  .band-blue { fill: var(--brand-blue); }
  .panel-dark { fill: var(--panel-dark); }
  .logo-dot { fill: var(--logo-blue); }
  .plate-white { fill: var(--card); }
</style>
</head>
<body>

<section class="card card--front" aria-label="Business card front">
  <svg viewBox="0 0 770 462" xmlns="http://www.w3.org/2000/svg">
    <!-- contact panel -->
    <polygon class="panel-dark" points="422,104 770,104 770,360 369,360"/>
    <!-- name band -->
    <polygon class="band-blue" points="0,177 424,177 392,281 384,289 0,289"/>

    <!-- brand -->
    <circle class="logo-dot" cx="92" cy="94" r="29"/>
    <text class="brand-name" x="128" y="103" font-size="24">HARLOW</text>

    <!-- staff -->
    <g class="icon" transform="translate(65,230)">
      <circle cx="0" cy="-6" r="5"/>
      <path d="M-10,9 C-10,1 -5,0 0,0 C5,0 10,1 10,9 Z"/>
    </g>
    <text class="staff-name" x="98" y="234">DANIEL PRYCE</text>
    <text class="staff-role" x="98" y="255">CEO</text>

    <!-- phone -->
    <path class="icon" transform="translate(447,151)" d="M4,1 L8,0 L11,6 L8,8 C9,11 12,14 15,15 L17,12 L23,15 L22,19 C20,21 16,21 12,18 C7,14 3,10 1,6 C0,4 1,2 4,1 Z"/>
    <text class="contact-line" x="491" y="169">555-014-2290</text>

    <!-- envelope -->
    <g transform="translate(447,192)">
      <rect class="icon" x="0" y="0" width="20" height="14"/>
      <path d="M0.5,0.5 L10,8 L19.5,0.5" fill="none" stroke="#1f1f21" stroke-width="1.6"/>
    </g>
    <text class="contact-line" x="491" y="207">info@harlowbody.com</text>

    <!-- globe -->
    <g transform="translate(457,240)" fill="none" stroke="#ffffff" stroke-width="1.6">
      <circle r="10"/>
      <ellipse rx="4.5" ry="10"/>
      <line x1="-10" y1="0" x2="10" y2="0"/>
      <path d="M-8.5,-5 H8.5 M-8.5,5 H8.5"/>
    </g>
    <text class="contact-line" x="491" y="248">www.harlowbody.com</text>

    <!-- pin -->
    <path class="icon" transform="translate(450,273)" d="M7,0 C11,0 14,3 14,7 C14,12 7,20 7,20 C7,20 0,12 0,7 C0,3 3,0 7,0 Z M7,4 A3,3 0 1 0 7.01,4 Z" fill-rule="evenodd"/>
    <text class="contact-line" x="491" y="290">218 Elmfield Road</text>
    <text class="contact-line" x="491" y="314">Oakridge,TX 70412</text>
  </svg>
</section>

<section class="card card--back" aria-label="Business card back">
  <svg viewBox="0 0 770 462" xmlns="http://www.w3.org/2000/svg">
    <rect class="band-blue" x="51" y="50" width="663" height="356"/>
    <rect class="plate-white" x="318" y="174" width="396" height="111"/>
    <circle class="logo-dot" cx="446" cy="229" r="37"/>
    <text class="brand-name" x="494" y="241" font-size="32">HARLOW</text>
  </svg>
</section>

</body>
</html>
```